BrushGuard Tolland- Making Helena A Wildfire Adapted Community

Design a two complimentary graphics with text that can be used for a banner and "mini-billboard" to promote the project and encourage citizens to go to the webpage to learn more. Using the attached document as examples of what we want the two banners to say.
The goal of BrushGuard Tolland is to plan and prepare so if an urban wildfire occurs, catastrophic loss can be avoided. BrushGuard Tolland focuses on reducing the risk of and catastrophic losses to resources and private property on private land in Helena, MT. Property owners are encouraged to be proactive to address hazardous fuel conditions on their property, reduce structure ignition potential within their home ignition zone and employ wildfire resilient principles to sustain a fire adapted home, property and community. Ember showers from a wildfire next to the city is the biggest concern.

Target Market(s)

Residents in the project area of Helena. Signs and banners will be displayed on public lands and private yeards

Font styles to use
Sans Serif

Requirements
Must have
• Graphics, use of the MeadowlineBlaze Watch Planning Circle logo. Must incorporate the text that is part of the attachment.
Nice to have
• Get people's attention. A simple graphic that get's people's attention.
Should not have
• small details.

```html
<!DOCTYPE html>
<html lang="en">
<head>
<meta charset="utf-8">
<title>Protect Your Home From Wildfire</title>
<link href="https://fonts.googleapis.com/css2?family=Open+Sans:wdth,wght@75..100,600..800&display=swap" rel="stylesheet">
<style>
  :root {
    --ink-dark: #150709;
    --ink-black: #050203;
    --white: #ffffff;
    --yellow: #ffe600;
    --fire-hot: #ffd23a;
    --fire-mid: #e88a12;
    --fire-deep: #7a2a08;
    --smoke: #3a1a0c;
  }
  * { margin: 0; padding: 0; box-sizing: border-box; }
  html, body { width: 1200px; height: 401px; overflow: hidden; background: var(--ink-dark); }
  .banner {
    position: relative;
    width: 1200px;
    height: 401px;
    background: var(--ink-dark);
    font-family: "Open Sans", Arial, sans-serif;
    font-stretch: 75%;
    font-weight: 700;
    overflow: hidden;
  }
  .scene {
    position: absolute;
    left: 350px; top: 0;
    width: 850px; height: 341px;
    background:
      radial-gradient(ellipse 170px 190px at 430px 130px, var(--fire-hot) 0%, var(--fire-mid) 45%, transparent 80%),
      radial-gradient(ellipse 200px 120px at 700px 40px, var(--fire-hot) 0%, var(--fire-mid) 50%, transparent 85%),
      radial-gradient(ellipse 260px 160px at 560px 280px, var(--fire-mid) 0%, var(--fire-deep) 60%, transparent 100%),
      linear-gradient(90deg, var(--ink-dark) 0%, var(--smoke) 25%, var(--fire-deep) 55%, #2a1206 100%);
  }
  .headline { position: absolute; left: 49px; color: var(--white); white-space: nowrap; line-height: 1; z-index: 2; }
  .headline--top { top: 30px; font-size: 52px; letter-spacing: -0.3px; }
  .headline--top span { display: block; }
  .headline--top span + span { margin-top: 7px; }
  .headline--accent { top: 160px; font-size: 80px; color: var(--yellow); letter-spacing: -0.3px; }
  .divider { position: absolute; left: 75px; top: 261px; width: 240px; height: 3px; background: var(--white); z-index: 2; }
  .subline { position: absolute; left: 49px; top: 288px; color: var(--white); font-size: 44px; line-height: 1; white-space: nowrap; letter-spacing: -0.3px; z-index: 3; }
  .subline span { display: block; }
  .subline span + span { margin-top: 8px; }
  .org-seal {
    position: absolute; left: 384px; top: 28px;
    width: 116px; height: 116px; border-radius: 50%;
    background: var(--white);
    display: flex; align-items: center; justify-content: center; text-align: center;
    z-index: 2;
  }
  .org-seal__name { color: var(--ink-dark); font-size: 15px; line-height: 1.1; padding: 0 10px; }
  .footer-strip {
    position: absolute; left: 335px; top: 341px;
    width: 865px; height: 60px;
    background: var(--ink-black);
    z-index: 1;
    white-space: nowrap;
    line-height: 1;
  }
  .footer-strip > span { position: absolute; top: 50%; transform: translateY(-50%); }
  .footer-strip__lead { left: 66px; color: var(--white); font-weight: 600; font-size: 36px; }
  .footer-strip__name { left: 282px; color: var(--yellow); font-size: 30px; letter-spacing: -0.3px; }
  .footer-strip__url { right: 22px; color: var(--yellow); font-weight: 600; font-size: 29px; }
</style>
</head>
<body>
  <div class="banner">
    <div class="scene" role="img" aria-label="Photo of a log house and shed engulfed in flames at night, trees and a fence in the foreground"></div>

    <h1 class="headline headline--top"><span>PROTECT YOUR</span><span>HOME FROM</span></h1>
    <div class="headline headline--accent">WILDFIRE</div>
    <div class="divider"></div>
    <p class="subline"><span>CREATE IGNITION</span><span>RESISTANT SPACE</span></p>

    <div class="org-seal"><span class="org-seal__name">MeadowlineBlaze Watch Planning Circle</span></div>

    <div class="footer-strip">
      <span class="footer-strip__lead">Learn more at</span>
      <span class="footer-strip__name">BRUSHGUARD TOLLAND</span>
      <span class="footer-strip__url">www.mbwatchcircle.org</span>
    </div>
  </div>
</body>
</html>
```